Brin-well Tide Port Custom Brokers Limited

Name: Loranda Pascoe
Title: Customs Broker
Address: Shop 9 Fernvale Commercial Complex
227-229 Marrow Lane
Kingston 8
Telephone: (876)
Email: tideportbrin@quillmail.example

```html
<!DOCTYPE html>
<html lang="en">
<head>
<meta charset="utf-8">
<title>Brin-well Tide Port Custom Brokers Limited – Business Cards</title>
<link rel="stylesheet" href="https://fonts.googleapis.com/css2?family=Lato:wght@400;700;900&display=swap">
<style>
  :root {
    --navy: #1b2a55;
    --gold: #e5a21a;
    --grey: #8a8f98;
    --card: #ffffff;
    --backdrop: #eceae6;
  }
  * { box-sizing: border-box; margin: 0; padding: 0; }
  html, body {
    width: 1200px;
    height: 800px;
    overflow: hidden;
    background: var(--backdrop);
    font-family: "Lato", sans-serif;
    color: var(--navy);
  }
  .sheet {
    width: 1200px;
    height: 800px;
    display: flex;
    align-items: center;
    justify-content: center;
    gap: 60px;
  }
  .card {
    width: 520px;
    height: 297px;
    background: var(--card);
    box-shadow: 0 6px 18px rgba(0, 0, 0, 0.12);
    display: flex;
    flex-direction: column;
    align-items: center;
    justify-content: center;
    text-align: center;
  }
  .brand {
    display: flex;
    align-items: center;
    gap: 10px;
  }
  .brand-dot {
    width: 16px;
    height: 16px;
    border-radius: 50%;
    background: var(--gold);
    flex: none;
  }
  .brand-name {
    font-weight: 900;
    text-transform: uppercase;
    color: var(--navy);
    line-height: 1.15;
    text-align: left;
  }
  .card--front .brand-name { font-size: 15px; letter-spacing: 0.5px; }
  .card--back .brand-name { font-size: 21px; letter-spacing: 0.8px; }
  .card--back .brand-dot { width: 22px; height: 22px; }

  .holder-name {
    margin-top: 22px;
    font-size: 22px;
    font-weight: 900;
    letter-spacing: 0.5px;
    text-transform: uppercase;
  }
  .holder-title {
    font-size: 14px;
    font-weight: 400;
    letter-spacing: 1px;
    text-transform: uppercase;
    margin-top: 2px;
  }
  .divider {
    width: 24px;
    height: 2px;
    background: var(--gold);
    margin: 10px 0 8px;
  }
  .contact {
    font-size: 13px;
    line-height: 1.45;
  }
  .address {
    margin-top: 2px;
    font-size: 12.5px;
    font-weight: 700;
    text-transform: uppercase;
    letter-spacing: 0.4px;
    line-height: 1.4;
  }
</style>
</head>
<body>
  <main class="sheet">
    <section class="card card--front" aria-label="Business card front">
      <div class="brand">
        <span class="brand-dot"></span>
        <span class="brand-name">Brin-well Tide Port<br>Custom Brokers Limited</span>
      </div>
      <h1 class="holder-name">Loranda Pascoe</h1>
      <p class="holder-title">Customs Broker</p>
      <span class="divider"></span>
      <p class="contact">(876)555 0142<br>tideportbrin@quillmail.example</p>
      <p class="address">Shop 9 Fernvale Commercial Complex<br>227-229 Marrow Lane, Kingston 8</p>
    </section>

    <section class="card card--back" aria-label="Business card back">
      <div class="brand">
        <span class="brand-dot"></span>
        <span class="brand-name">Brin-well Tide Port<br>Custom Brokers Limited</span>
      </div>
    </section>
  </main>
</body>
</html>
```